Packaging design pot 500gr Polynesian honey

Task Description

Concept of design:

"This Polynesian island is a small piece of paradise nestled in the South Pacific, away from any form of civilization ( ideal place for producing honey of excellence )
= Images / symbols that induces dreaming)); (100% organic, 100% natural organic Honey logo)
Elegant, subtle , eyes catching, NO pictures of bees , Simple colors: BLACK, GOLD, WHITE, tranparency . (Designer discretion)
(Bio label optional )

the Labels: Hex1 product of TAHITI header: VELINOA HONEY (brand name) MAY USE all images herein below , free of copyright (Macro coconut flower, coconut white sand beach, exoticism; 500 gr; text on back (see attached text); Position the bar code vertically on the back; Mandatory address: Website on the back, infocontact, registration number.

500g pot :
HEIGHT With cap 12.00cm Without cap 11.85 cm
outside diameter 7.24cm
Label height should only be = 5, 1 cm x height
See the container with black cap.

Deadline
March 15, 2018 ( postpone if needed )
Updates

To all participants, i have added a personal photo you may want to consider in your creative process. If the upper section of the photo is exploited, I thought it has something interesting to bring: blue sky on the background including a shadow ot the coconut leaves, ( no bees please).

Finally i have added the colour of Velinoa Honey

Dear participants, I have updated two files to be taken into account onward : 1) final text: in French ; the replicate is English for the English version valid with the identical Graphic design 2) the true colours of Velinoa Honey, for your consideration. I thought that with the help of day light i could enhance its true body colour. Best regards, Mr KOR

Target Market(s)

Target the Asian market , Onward The US MARKET, (LUXURY oriented)

Font styles to use
Serif

Colors

Designer to choose colors to be used in the design.

Requirements
Must have
• Website address on the back, infocontact, registration number,
• texte ( summary )
• coconut tree honey ( ORIGIN )
• Color code : BLACK , GOLD , light , transparency
• COLORS THAT MATCH COLOR OF THE HONEY : DARK RED AMBER SEE IMAGE ATTACHED
Nice to have
• A matching logo
• A 400g Squezze bottle format ;
• h18.5*d7.8*c3.2(cm)
Should not have
• No Bees

```html
<!DOCTYPE html>
<html lang="fr">
<head>
<meta charset="utf-8">
<title>Cocotier – Miel de fleur – Velinoa Honey</title>
<link rel="stylesheet" href="https://fonts.googleapis.com/css2?family=Josefin+Slab:wght@700&family=Lato:wght@300;400;700&display=swap">
<style>
  :root {
    --label-black: #141414;
    --band-black: #1d1d1d;
    --gold: #e0a33a;
    --gold-soft: #c98a2a;
    --white: #ffffff;
    --text-grey: #d8d8d8;
    --backdrop: #efeae2;
    --flower-dark: #1a1712;
    --flower-light: #e9c77a;
  }
  * { box-sizing: border-box; margin: 0; padding: 0; }
  html, body {
    width: 1200px; height: 795px; overflow: hidden;
    background: var(--backdrop);
    font-family: "Lato", Arial, sans-serif;
  }
  .canvas { position: relative; width: 1200px; height: 795px; }

  /* Front label */
  .front { position: absolute; left: 170px; top: 215px; width: 380px; height: 430px; }
  .cap-strip {
    position: absolute; left: 159px; top: -190px; width: 62px; height: 220px;
    background: var(--band-black); border-left: 2px solid var(--gold); border-right: 2px solid var(--gold);
  }
  .cap-strip-text {
    position: absolute; left: 0; right: 0; top: 12px; height: 135px;
    writing-mode: vertical-rl; transform: rotate(180deg);
    display: flex; flex-direction: column; align-items: center; justify-content: center;
    white-space: nowrap; line-height: 1.1;
  }
  .cap-strip-name { font-family: "Josefin Slab", Georgia, serif; font-weight: 700; color: var(--white); font-size: 19px; letter-spacing: 1px; }
  .cap-strip-sub { color: var(--gold); font-weight: 300; font-size: 16px; }
  .front-body {
    position: absolute; inset: 0; background: var(--label-black);
    display: flex; flex-direction: column; align-items: center;
  }
  .brand-mark {
    margin-top: -34px; width: 80px; height: 80px; border-radius: 50%;
    background: var(--label-black); border: 3px solid var(--gold);
    display: flex; align-items: center; justify-content: center;
    font-weight: 700; font-size: 10px; letter-spacing: 0.5px; color: var(--gold); text-align: center; line-height: 1.2;
    position: relative; z-index: 1;
  }
  .product-name { margin-top: 16px; font-family: "Josefin Slab", Georgia, serif; font-weight: 700; font-size: 30px; letter-spacing: 2px; color: var(--white); }
  .product-type { margin-top: 4px; font-weight: 300; font-size: 26px; color: var(--gold); }
  .origin { margin-top: 8px; font-size: 12px; color: var(--text-grey); }
  .flower-photo {
    margin-top: 14px; width: 100%; flex: 1;
    background: radial-gradient(ellipse at 60% 45%, var(--flower-light) 0%, #b8924a 30%, #3a3224 62%, var(--flower-dark) 100%);
  }

  /* Back label */
  .back {
    position: absolute; left: 590px; top: 215px; width: 440px; height: 430px;
    background: var(--label-black); padding: 34px 28px; display: flex; gap: 24px;
  }
  .back-info { width: 170px; font-size: 9.5px; line-height: 1.55; color: var(--text-grey); }
  .back-info strong { color: var(--white); font-weight: 700; }
  .back-info p { margin-bottom: 8px; }
  .back-info .best-before { margin-top: 190px; }
  .back-story { flex: 1; }
  .back-title { font-weight: 700; font-size: 14px; color: var(--gold); margin-bottom: 12px; }
  .back-text { font-size: 9.5px; line-height: 1.65; color: var(--text-grey); }
</style>
</head>
<body>
<main class="canvas">

  <section class="front" aria-label="Étiquette avant">
    <div class="cap-strip">
      <div class="cap-strip-text">
        <span class="cap-strip-name">COCOTIER</span>
        <span class="cap-strip-sub">Miel de fleur</span>
      </div>
    </div>
    <div class="front-body">
      <div class="brand-mark">VELINOA<br>HONEY</div>
      <h1 class="product-name">COCOTIER</h1>
      <p class="product-type">Miel de fleur</p>
      <p class="origin">Tahiti</p>
      <div class="flower-photo" role="img" aria-label="Photo macro d'une fleur de cocotier dorée avec une goutte de miel"></div>
    </div>
  </section>

  <section class="back" aria-label="Étiquette arrière">
    <div class="back-info">
      <p><strong>Ingrédients :</strong> Miel de Velinoa</p>
      <p>Conserver à moins de <strong>25°</strong> dans un endroit frais et sec.</p>
      <p><strong>Ne pas utiliser si le bouchon est cassé.</strong></p>
      <p>Velinoa Island BP 1024 PAPEETE TAHITI 98700 FRENCH POLYNESIA</p>
      <p>velinoahoney.com<br>info@velinoahoney.com</p>
      <p>Velinoa Honey 蜂蜜 عسل</p>
      <p class="best-before">A consommer avant : lire sur l'étiquette</p>
    </div>
    <div class="back-story">
      <h2 class="back-title">Miel de Velinoa</h2>
      <p class="back-text">Le miel de Velinoa est récolté sur un atoll isolé du Pacifique Sud, loin de toute pollution. Nos abeilles butinent librement les fleurs de cocotier sous un soleil généreux. Ce miel doré, doux et parfumé, est extrait à froid et mis en pot sans aucun traitement afin de préserver toute sa richesse naturelle.</p>
    </div>
  </section>

</main>
</body>
</html>
```